Travel Poster Design Project

A poster design for a specific Adventure Travel Journey to Ladakh India. The journey it will be promoting is a 2 week trekking and cultural tour through Ladakh passing over 2 mountain passes in excess of 5000 meters.

Dates are July and August each year

Brand Name is Farwind Treks

We do inspiring unique journeys in a small select number of locations around the world. Ladakh is also known as Little Tibet and has a buddhist culture

We have a logo already to use and we also have a range of photos online for you to select from. They can be seen at http://images.brookpaddle.example/FarwindTreks then click on Ladakh

Target Market(s)

Adventure travel people 30-55 poster will be displayed in our rafting retail base so will be seen by target market

Industry/Entity Type

Travel

Requirements
Must have
• website address www.farwindtreks.example
Phone Number 01632 960418
email info@farwindtreks.example
Pictures
small legal note along the bottom, saying Farwind Treks is a brand name of Torrent Ridge River Sports LLP
Nice to have
• Lots of inspiring photos and colour
Should not have
• named dates

```html
<!DOCTYPE html>
<html lang="en">
<head>
<meta charset="utf-8">
<title>Adventure Travel Journey to Ladakh, India – Farwind Treks</title>
<link rel="stylesheet" href="https://fonts.googleapis.com/css2?family=Open+Sans:wght@400;700;800&family=Sancreek&display=swap">
<style>
  :root {
    --ink: #000000;
    --band: #0b0b0b;
    --scroll: #1c1c1c;
    --white: #ffffff;
    --gold-hi: #f3d78a;
    --gold-lo: #a9782a;
    --blue: #1aa3e0;
    --orange: #f57f20;
    --green: #1faa4a;
    --magenta: #e6198a;
    --red: #ec2227;
    --yellow: #fff200;
  }
  * { box-sizing: border-box; margin: 0; padding: 0; }
  html, body { width: 848px; height: 1200px; overflow: hidden; background: var(--ink); }
  .poster {
    position: relative;
    width: 848px;
    height: 1200px;
    background: var(--ink);
    font-family: "Open Sans", Arial, sans-serif;
    color: var(--white);
    overflow: hidden;
  }
  .photo-row { position: absolute; left: 0; width: 848px; display: flex; }
  .photo-row--top { top: 0; height: 449px; }
  .photo-row--bottom { top: 749px; height: 278px; }
  .photo { height: 100%; flex: 1 1 0; }
  .photo--stupa { background: linear-gradient(180deg, #2f7fd6 0%, #8dbbe8 35%, #f1f1ee 60%, #d9d6cf 100%); }
  .photo--buddha { background: radial-gradient(ellipse at 50% 40%, #e2b44a 0%, #c08a2c 40%, #7a3a20 75%, #3a2a3a 100%); }
  .photo--valley { background: linear-gradient(180deg, #7fb0e4 0%, #c9a98a 18%, #b08c6c 45%, #3f6a2c 62%, #2c4f22 100%); }
  .photo--murals { background: linear-gradient(135deg, #c96d2a 0%, #2f8c8a 45%, #d08a3a 100%); }
  .photo--chorten { background: linear-gradient(180deg, #3d7fd0 0%, #a8c9ee 45%, #e2ddd2 70%, #9a6a4a 100%); }
  .photo--flags { background: linear-gradient(160deg, #5a3d28 0%, #c9b58e 35%, #3b6fb6 55%, #d9342a 75%, #6a4a30 100%); }
  .photo--doorway { background: linear-gradient(180deg, #8a2c22 0%, #6b4a34 30%, #c8bca8 60%, #4e3a2a 100%); }
  .photo--stream { background: linear-gradient(180deg, #9fc0e4 0%, #8d8a80 35%, #5c7048 60%, #9aa8a6 100%); }

  .gold-rule {
    position: absolute; left: 0; width: 848px; height: 4px;
    background: linear-gradient(90deg, var(--gold-lo), var(--gold-hi) 30%, var(--gold-lo) 60%, var(--gold-hi) 85%, var(--gold-lo));
  }
  .gold-rule--a { top: 449px; }
  .gold-rule--b { top: 745px; }
  .gold-rule--c { top: 1027px; }

  .title-band { position: absolute; top: 453px; left: 0; width: 848px; height: 292px; background: var(--band); }
  .scroll-band { position: absolute; left: 0; width: 848px; height: 50px; background: var(--scroll); }
  .scroll-band--upper { top: 8px; }
  .scroll-band--lower { top: 226px; }

  .kicker {
    position: absolute; top: 12px; left: 66px;
    font-weight: 700; font-size: 31px; letter-spacing: -0.2px;
  }
  .destination {
    position: absolute; top: 48px; left: 0; width: 848px; text-align: center;
    font-family: "Sancreek", "Georgia", serif; font-size: 178px; line-height: 1;
    letter-spacing: 2px;
  }
  .destination span:nth-child(1) { color: var(--blue); }
  .destination span:nth-child(2) { color: var(--orange); }
  .destination span:nth-child(3) { color: var(--green); }
  .destination span:nth-child(4) { color: var(--magenta); }
  .destination span:nth-child(5) { color: var(--red); }
  .destination span:nth-child(6) { color: var(--yellow); }
  .country {
    position: absolute; top: 234px; right: 56px;
    font-weight: 400; font-size: 42px; letter-spacing: 17px;
  }

  .footer { position: absolute; top: 1031px; left: 0; width: 848px; height: 169px; background: var(--ink); }
  .contact { position: absolute; left: 26px; top: 67px; font-size: 17px; line-height: 24px; }
  .contact dt { display: inline-block; width: 70px; }
  .contact dd { display: inline; }
  .legal { position: absolute; left: 26px; top: 135px; font-size: 13px; }
  .brand {
    position: absolute; left: 554px; top: 22px;
    display: flex; align-items: center; gap: 12px;
    font-weight: 700; font-size: 26px;
  }
  .brand-dot { width: 74px; height: 74px; border-radius: 50%; border: 3px solid var(--white); }
  .website { position: absolute; right: 24px; top: 122px; font-weight: 700; font-size: 22px; }
</style>
</head>
<body>
<main class="poster">
  <div class="photo-row photo-row--top">
    <div class="photo photo--stupa" role="img" aria-label="Photo of a white Buddhist stupa against a blue sky"></div>
    <div class="photo photo--buddha" role="img" aria-label="Photo of a golden Buddha statue in a monastery"></div>
    <div class="photo photo--valley" role="img" aria-label="Photo of a hillside monastery above a green valley with a white chorten"></div>
  </div>
  <div class="gold-rule gold-rule--a"></div>

  <section class="title-band">
    <div class="scroll-band scroll-band--upper" role="img" aria-label="Dark scroll ornament band"></div>
    <div class="scroll-band scroll-band--lower" role="img" aria-label="Dark scroll ornament band"></div>
    <p class="kicker">Adventure Travel Journey to</p>
    <h1 class="destination"><span>L</span><span>A</span><span>D</span><span>A</span><span>K</span><span>H</span></h1>
    <p class="country">INDIA</p>
  </section>

  <div class="gold-rule gold-rule--b"></div>
  <div class="photo-row photo-row--bottom">
    <div class="photo photo--murals" role="img" aria-label="Photo of painted Buddha murals on a monastery wall"></div>
    <div class="photo photo--chorten" role="img" aria-label="Photo of a whitewashed chorten under a blue sky"></div>
    <div class="photo photo--flags" role="img" aria-label="Photo of colourful prayer flags strung across a courtyard"></div>
    <div class="photo photo--doorway" role="img" aria-label="Photo of a monastery doorway and old stone buildings"></div>
    <div class="photo photo--stream" role="img" aria-label="Photo of a mountain stream in a rocky valley"></div>
  </div>
  <div class="gold-rule gold-rule--c"></div>

  <footer class="footer">
    <dl class="contact">
      <div><dt>Phone:</dt><dd>01632 960418</dd></div>
      <div><dt>Email:</dt><dd>info@farwindtreks.example</dd></div>
    </dl>
    <p class="legal">Farwind Treks is a brand name of Torrent Ridge River Sports LLP</p>
    <div class="brand">
      <span class="brand-dot"></span>
      <span class="brand-name">Farwind Treks</span>
    </div>
    <p class="website">www.farwindtreks.example</p>
  </footer>
</main>
</body>
</html>
```